Business Card

Need a clean, professional, simple, but clever business card for our company LUX RIDES. We only want to see black and white colors as that reflects the branding of our company. Attaching logo. Will also consider the "sky blue" shown in our web site sample png - but use of the color should be minimal.

Lux Rides is a executive car service operating in cities throughout Africa. By operating well equipped Valdren Oster vehicles, we offer the smoothest and stylish ride in town. We aim to provide customers with a valuable experience. That’s why we make sure our patrons get picked up like a boss, travel in style, and arrive fabulous.

We need a card that says that. Likely to print on the best quality/smoothest paper available, as it must speak volumes of our business and class.

We would like the rear of the card to be all black. Perhaps we can put the web url on it, or leave it blank if it looks neater/more elegant.

Use the following contact information (as you see fit):

Lux Rides Limited
P.O. Box 47106
Dar es Salaam, Tanzania

Baraka Kilonzo
Managing Director

+255 (0) 754 829016
sales@luxrides-demo.co.tz

web url: www.luxrides-demo.co.tz
email: chauffeur@luxrides-demo.co.tz

***Winning designer will likely be commissioned for more promotional work in near future.

Target Market(s)

The target market for this card is corporate executives of top firms (financial, consulting, businessmen, etc). They are interested in high quality transportation. Our fleet is all high end Valdren Oster black cars (black exterior, black interior); and therefore, that high end quality and promptness must be reflected in the card. Also simplicity, as we we take care of all the little details behind the scene.

Industry/Entity Type

Business

Requirements
Must have
• Font must be: Helvetica Neue, like the logo. You may use other variations (Thin, Ultra thin, Regular, Bold), so long as it looks and prints well.

If web url is included on the back of the card, then do NOT include it also on the front.
Nice to have
• If there is something nice and clever that you can do/think of that doesn't make the card look busy, but adds a little "posh", then I could be even more interested.

However, if there's no little thing do be done, I'd rather a simple, but very professional looking card that attracts a lot of attention.

```html
<!DOCTYPE html>
<html lang="en">
<head>
<meta charset="utf-8">
<title>Lux Rides – Business Card</title>
<link href="https://fonts.googleapis.com/css2?family=Arimo:wght@400;700&display=swap" rel="stylesheet">
<style>
  :root {
    --sky: #2bbad6;
    --ink: #1d1d1d;
    --muted: #3a3a3a;
    --paper: #ffffff;
    --black: #111111;
    --stage: #e9e9e9;
    --rule: #d6d6d6;
  }
  * { box-sizing: border-box; margin: 0; padding: 0; }
  html, body { width: 1200px; height: 871px; overflow: hidden; }
  body {
    background: var(--stage);
    font-family: "Arimo", "Helvetica Neue", Helvetica, Arial, sans-serif;
    color: var(--ink);
    position: relative;
  }
  .card {
    position: absolute;
    left: 320px;
    width: 560px;
    height: 320px;
    box-shadow: 0 6px 18px rgba(0,0,0,.18);
  }
  /* Back side: all black */
  .card-back {
    top: 80px;
    background: var(--black);
    color: var(--paper);
    display: flex;
    flex-direction: column;
    align-items: center;
    justify-content: center;
  }
  .card-back .brand-name {
    font-size: 32px;
    font-weight: 400;
    letter-spacing: 3px;
  }
  .card-back .web-url {
    margin-top: 6px;
    font-size: 11px;
    letter-spacing: 1.5px;
  }
  /* Front side */
  .card-front {
    top: 470px;
    background: var(--paper);
  }
  .accent-bar {
    position: absolute;
    width: 20px;
    background: var(--sky);
  }
  .accent-bar.left  { left: 0;  top: 115px; height: 195px; }
  .accent-bar.right { right: 0; top: 18px;  height: 190px; }
  .divider {
    position: absolute;
    left: 268px;
    top: 40px;
    width: 1px;
    height: 230px;
    background: var(--rule);
  }
  .card-front .brand-name {
    position: absolute;
    left: 56px;
    top: 143px;
    font-size: 26px;
    font-weight: 400;
    letter-spacing: 2.5px;
    color: var(--ink);
  }
  .contact {
    position: absolute;
    left: 296px;
    top: 48px;
    width: 230px;
  }
  .person-name {
    font-size: 19px;
    font-weight: 700;
    letter-spacing: 1.5px;
  }
  .person-role {
    font-size: 9.5px;
    letter-spacing: 1px;
    margin: 3px 0 0 8px;
    color: var(--muted);
  }
  .contact-list { list-style: none; margin-top: 18px; font-size: 12px; line-height: 1.3; }
  .contact-list li { display: flex; gap: 8px; align-items: flex-start; }
  .contact-list li + li { margin-top: 3px; }
  .contact-list li.gap { margin-top: 14px; }
  .contact-list svg { flex: none; width: 12px; height: 12px; margin-top: 2px; fill: var(--sky); }
</style>
</head>
<body>

<section class="card card-back" aria-label="Card back">
  <div class="brand-name">LUX RIDES</div>
  <div class="web-url">WWW.LUXRIDES-DEMO.CO.TZ</div>
</section>

<section class="card card-front" aria-label="Card front">
  <div class="accent-bar left"></div>
  <div class="accent-bar right"></div>
  <div class="brand-name">LUX RIDES</div>
  <div class="divider"></div>

  <div class="contact">
    <div class="person-name">BARAKA KILONZO</div>
    <div class="person-role">MANAGING DIRECTOR</div>
    <ul class="contact-list">
      <li>
        <svg viewBox="0 0 12 12" aria-hidden="true"><path d="M6 1 0.5 6H2v5h3V8h2v3h3V6h1.5z"/></svg>
        <span>Lux Rides Limited,<br>P.O. Box 47106,<br>Dar es Salaam, Tanzania</span>
      </li>
      <li class="gap">
        <svg viewBox="0 0 12 12" aria-hidden="true"><path d="M1 4.5C1 3 2.5 2 6 2s5 1 5 2.5V5.5H8.5V4.3h-5V5.5H1zM2.5 6.5h7L10.5 10h-9z"/></svg>
        <span>+255 (0) 754 829016</span>
      </li>
      <li>
        <svg viewBox="0 0 12 12" aria-hidden="true"><path d="M1 2.5h10v7H1z M1.6 3 6 6.5 10.4 3" stroke="#fff" stroke-width=".8"/></svg>
        <span>chauffeur@luxrides-demo.co.tz</span>
      </li>
    </ul>
  </div>
</section>

</body>
</html>
```